Letterhead Design

I would like 2 different letterheads. One with each logo I have attached. Business info:
Prairieline Medical Billing, LLC
4830 N Alder
Dunmore, KS 66923
(866) 555-0143

```html
<!DOCTYPE html>
<html lang="en">
<head>
<meta charset="utf-8">
<title>Prairieline Medical Billing – Letterheads</title>
<link href="https://fonts.googleapis.com/css2?family=Crimson+Pro:wght@400&display=swap" rel="stylesheet">
<style>
  :root {
    --paper: #fefefc;
    --band-purple: #4a3f85;
    --rule-red: #b3312c;
    --teal: #3a9ca6;
    --gold: #cbb27c;
    --slate: #3d4a4f;
    --white: #ffffff;
  }
  * { margin: 0; padding: 0; box-sizing: border-box; }
  html, body { width: 1200px; height: 835px; overflow: hidden; background: var(--paper); }
  body { font-family: "Crimson Pro", "Times New Roman", serif; position: relative; }

  .sheet { position: absolute; top: 0; height: 835px; }
  .sheet--banded { left: 0; width: 591px; }
  .sheet--ruled { left: 610px; width: 590px; }

  .header-band {
    position: absolute; left: 0; top: 0; width: 591px; height: 114px;
    background: var(--band-purple);
  }
  .header-rule {
    position: absolute; left: 0; top: 117px; width: 591px; height: 4px;
    background: var(--rule-red);
  }

  .brand-mark { position: absolute; display: flex; flex-direction: column; align-items: center; }
  .brand-mark__dot { border-radius: 50%; }
  .brand-mark__name { line-height: 1; margin-top: 6px; }

  .sheet--banded .brand-mark { left: 22px; top: 18px; width: 90px; }
  .sheet--banded .brand-mark__dot { width: 58px; height: 58px; background: var(--gold); }
  .sheet--banded .brand-mark__name { color: var(--white); font-size: 14px; }

  .company { position: absolute; text-align: right; }
  .company__name { font-weight: 400; line-height: 1; white-space: nowrap; }
  .company__line { line-height: 1; white-space: nowrap; }

  .sheet--banded .company { right: 33px; top: 22px; color: var(--white); }
  .sheet--banded .company__name { font-size: 27px; margin-bottom: 9px; }
  .sheet--banded .company__line { font-size: 17px; margin-bottom: 1px; }

  .margin-rule {
    position: absolute; left: 34px; top: 0; width: 4px; height: 835px;
    background: var(--rule-red);
  }
  .top-rule {
    position: absolute; left: 0; top: 103px; width: 590px; height: 4px;
    background: var(--rule-red);
  }
  .sheet--ruled .brand-mark { left: 46px; top: 20px; width: 72px; }
  .sheet--ruled .brand-mark__dot { width: 44px; height: 44px; background: var(--slate); }
  .sheet--ruled .brand-mark__name { color: var(--slate); font-size: 12px; }

  .sheet--ruled .company { right: 36px; top: 19px; color: var(--teal); }
  .sheet--ruled .company__name { font-size: 27px; margin-bottom: 4px; }
  .sheet--ruled .company__line { font-size: 15.5px; margin-bottom: 1px; }
</style>
</head>
<body>
  <section class="sheet sheet--banded" aria-label="Letterhead, purple band version">
    <div class="header-band"></div>
    <div class="header-rule"></div>
    <div class="brand-mark">
      <span class="brand-mark__dot"></span>
      <span class="brand-mark__name">Prairieline</span>
    </div>
    <address class="company" style="font-style:normal">
      <h1 class="company__name">Prairieline Medical Billing, LLC</h1>
      <p class="company__line">4830 N Alder</p>
      <p class="company__line">Dunmore, KS 66923</p>
      <p class="company__line">(866) 555-0143</p>
    </address>
  </section>

  <section class="sheet sheet--ruled" aria-label="Letterhead, ruled margin version">
    <div class="top-rule"></div>
    <div class="margin-rule"></div>
    <div class="brand-mark">
      <span class="brand-mark__dot"></span>
      <span class="brand-mark__name">Prairieline</span>
    </div>
    <address class="company" style="font-style:normal">
      <h1 class="company__name">Prairieline Medical Billing, LLC</h1>
      <p class="company__line">4830 N Alder</p>
      <p class="company__line">Dunmore, KS 66923</p>
      <p class="company__line">(866) 555-0143</p>
    </address>
  </section>
</body>
</html>
```